business card with logo Marigold Nails & Spa 2815 SW Harlow Ave Portland OR 97099

Would like to have a business card with our logo.
like bottle of polish with our logo or letter M on it
want something that first glance would let you know that it is a nail salon.
like the hands with polish bottle dripping.
like black or White back ground

Marigold Nails & Spa
(The Velvet Retreat)
2815 SW Harlow Ave
Portland, OR 97099
Call or Text: 1-555-714-3928
www.MarigoldNailsnSpa.example
Open 7 days a week.
After 7:00 PM is by appointment only.
Closed only on Thanksgiving & Christmas.

Target Market(s)

20%Man and 80%Woman 13-70

Industry/Entity Type

Business

Contact Information for Business Card

Elegant with Logo-Business name- address-phone-open days. closed day.

Font styles to use
Decorative
Script

Colors
000000

Requirements
Must have
• Logo and place for Technician Name
• Marigold Nails & Spa
• (The Velvet Retreat)
• 2815 SW Harlow Ave
• Portland, OR 97099
• Call or Text: 1-555-714-3928
• Open 7 days a week
• Closed only on Thanksgiving & Christmas.
• We accepted all major credit cards but prefer cash. Thank you
Nice to have
• Nail polish bottle with our Logo or letter M
Should not have
• too colorful

```html
<!DOCTYPE html>
<html lang="en">
<head>
<meta charset="utf-8">
<title>Marigold Nails &amp; Spa — Business Card</title>
<link rel="stylesheet" href="https://fonts.googleapis.com/css2?family=Great+Vibes&family=Roboto:wght@300;400;500;700&display=swap">
<style>
  :root {
    --bg: #e9e7e3;
    --card: #ffffff;
    --card-shade: #ececec;
    --ink: #1a1a1a;
    --ink-soft: #333333;
    --lime: #b6d335;
    --lime-deep: #9fc21f;
    --blush: #f6c3c6;
    --blush-light: #fbe3e4;
  }
  * { box-sizing: border-box; margin: 0; padding: 0; }
  html, body {
    width: 1200px; height: 1023px; overflow: hidden;
    background: var(--bg);
    font-family: "Roboto", Arial, sans-serif;
    color: var(--ink);
  }
  .canvas { position: relative; width: 1200px; height: 1023px; }
  .card {
    position: absolute; left: 100px; top: 225px;
    width: 1000px; height: 572px;
    border-radius: 26px; overflow: hidden;
    background: radial-gradient(ellipse at 40% 45%, var(--card) 0%, var(--card) 55%, var(--card-shade) 100%);
    box-shadow: 0 18px 40px rgba(0,0,0,.18);
  }
  .polish-photo {
    position: absolute; left: 420px; top: 60px; width: 230px; height: 100px;
    border-radius: 12px;
    background: linear-gradient(90deg, #f2f2f2 0%, #ffffff 40%, var(--blush-light) 55%, var(--blush) 100%);
  }
  .swoosh { position: absolute; inset: 0; }

  .brand { position: absolute; left: 60px; top: 150px; display: flex; align-items: center; gap: 16px; }
  .brand-mark { width: 20px; height: 20px; border-radius: 50%; background: var(--ink); }
  .brand-name { font-family: "Great Vibes", cursive; font-size: 110px; font-weight: 400; line-height: 1; }
  .brand-sub {
    position: absolute; left: 110px; top: 282px;
    display: flex; align-items: center; gap: 10px;
    font-size: 30px; font-weight: 400; color: var(--lime-deep);
  }
  .brand-sub::before, .brand-sub::after {
    content: ""; width: 40px; height: 2px; background: var(--ink);
  }
  .brand-tag {
    position: absolute; left: 110px; top: 326px;
    font-size: 27px; font-weight: 300; color: var(--ink-soft); letter-spacing: .5px;
  }

  .hours { position: absolute; right: 40px; top: 236px; text-align: right; font-size: 18px; line-height: 1.75; }
  .hours li { list-style: none; }
  .hours li::after {
    content: ""; display: inline-block; width: 7px; height: 7px; border-radius: 50%;
    background: var(--lime); margin-left: 10px; vertical-align: middle;
  }
  .payment { position: absolute; right: 40px; top: 318px; text-align: right; }
  .payment-note { font-size: 14px; font-weight: 500; }
  .payment-list { display: flex; justify-content: flex-end; gap: 22px; margin-top: 14px; }
  .payment-list span { font-size: 17px; font-weight: 700; color: var(--ink); }

  .contact {
    position: absolute; left: 460px; top: 448px;
    font-style: normal; font-size: 20px; font-weight: 400; line-height: 1.35;
  }
  .contact-row { display: flex; align-items: flex-start; gap: 12px; margin-bottom: 6px; }
  .contact-row svg { flex: none; margin-top: 3px; }
</style>
</head>
<body>
<main class="canvas">
  <section class="card" aria-label="Business card front">
    <div class="polish-photo" role="img" aria-label="Pink nail polish bottle with white brush cap"></div>

    <svg class="swoosh" width="1000" height="572" viewBox="0 0 1000 572" aria-hidden="true">
      <path d="M640,0 C660,140 600,230 500,310 C410,385 368,450 370,572 L408,572 C408,470 450,410 540,335 C640,250 712,150 712,0 Z" fill="var(--lime)"/>
    </svg>

    <div class="brand">
      <span class="brand-mark"></span>
      <span class="brand-name">Marigold</span>
    </div>
    <p class="brand-sub">Nails &amp; Spa</p>
    <p class="brand-tag">The Velvet Retreat</p>

    <ul class="hours">
      <li>Open 7 days a week</li>
      <li>Closed only on Thanksgiving &amp; Christmas</li>
    </ul>

    <div class="payment">
      <p class="payment-note">We accepted all major credit cards but prefer cash</p>
      <div class="payment-list">
        <span>Vantra</span><span>Mintcard</span><span>Ambrex</span><span>Dovecard</span>
      </div>
    </div>

    <address class="contact">
      <div class="contact-row">
        <svg width="20" height="20" viewBox="0 0 20 20"><circle cx="10" cy="10" r="9" fill="none" stroke="var(--lime-deep)" stroke-width="1.6"/><path d="M7 5.5c-.8.6-1 1.6-.5 2.8.8 1.9 2.3 3.4 4.2 4.2 1.2.5 2.2.3 2.8-.5l-1.6-1.5-1.2.7c-1-.5-1.8-1.3-2.3-2.3l.7-1.2Z" fill="var(--lime-deep)"/></svg>
        <span>1-555-714-3928</span>
      </div>
      <div class="contact-row">
        <svg width="20" height="24" viewBox="0 0 20 24"><path d="M10 1C5.6 1 2.5 4.2 2.5 8.4 2.5 14 10 23 10 23s7.5-9 7.5-14.6C17.5 4.2 14.4 1 10 1Z" fill="var(--lime-deep)"/><circle cx="10" cy="8.5" r="3" fill="#fff"/></svg>
        <span>2815 SW Harlow Ave<br>Portland, OR 97099</span>
      </div>
    </address>
  </section>
</main>
</body>
</html>
```